Summit Institute Binder Cover and Spine Design

Design of 1 Binder Cover and Spine -
Dimensions for Colored Print:
Front Cover: 11 1/16 H x 11 1/8 W
Spine: 11 1/16 H x 2 3/8 W
Our Summit Institute link for more information about the course and the topics covered, as well the background of NCLFA (National Council of Levy Fixers Alliance). Please take the time to view our website, including the Summit Institute page to get a background of what the course covers. The website will give you a great feel for what we like in design elements, simple and professional.
https://www.nclfa-example.org/levy-fix-institute/
Must be included: Blue Logos (all 3)
Words to be included- Summit Institute (Large- title of course)
-FRB Tax Problem Resolution (Small/Medium Font)
This course attendance includes accountants, Certified Public Accountants, Enrolled Agents, Attorneys and tax professionals. The Summit Institute instructs them on high level topics of Tax Resolution- which in short is to learn how to legally advocate for your clients and help those with Tax Problems against the FRB.
Attached is our Groundwork Binder Cover- this is the prerequisite course for the Summit Institute. We like this design but are looking for something that would be sharper, cleaner and more advanced appeal. This is a professional course and would like the binder cover and spine to reflect that.
Attached are a variety of logos as well. The CPE Logo must be used for our accreditation for the FRB. We do not want any dates on the Binder so we can use over again.
Updates
The design we choose, we will need the print PDF as well as the Raw Design File incase we need to edit for size or print.
Target Market(s)

```html
<!DOCTYPE html>
<html lang="en">
<head>
<meta charset="utf-8">
<title>Summit Institute — Binder Cover and Spine</title>
<link href="https://fonts.googleapis.com/css2?family=Montserrat:wght@300;400;600;800;900&display=swap" rel="stylesheet">
<style>
  :root{
    --navy:#2a5a95;
    --royal:#1f6cb3;
    --sky:#0aa9df;
    --tint:#5fb6e3;
    --title:#2b5c94;
    --subtitle:#1b86c6;
    --paper:#ffffff;
    --stage:#f4f5f7;
    --badge:#8a86b8;
    --photo-a:#3b4a5c;
    --photo-b:#c9d3dc;
  }
  *{margin:0;padding:0;box-sizing:border-box}
  html,body{width:1200px;height:842px;overflow:hidden}
  body{background:var(--stage);font-family:"Montserrat",Arial,sans-serif;position:relative}

  .binder{position:absolute;left:203px;top:101px;height:640px;display:flex;gap:12px}

  .spine{position:relative;width:138px;height:640px;background:var(--paper);overflow:hidden;box-shadow:0 1px 3px rgba(0,0,0,.08)}
  .spine__shapes{position:absolute;inset:0;width:100%;height:100%}
  .spine__mark{position:absolute;top:62px;left:69px;transform:translate(-50%,-50%) rotate(90deg);
    color:var(--paper);font-weight:600;font-size:15px;letter-spacing:1px;white-space:nowrap}
  .spine__title{position:absolute;left:69px;top:485px;transform:translate(-50%,-50%) rotate(90deg);
    color:var(--title);font-weight:900;font-size:36px;line-height:1;letter-spacing:.5px;white-space:nowrap;text-align:left}
  .spine__band,.cover__band{position:absolute;left:0;right:0;bottom:0;height:13px;background:var(--navy)}

  .cover{position:relative;width:644px;height:640px;background:var(--paper);overflow:hidden;box-shadow:0 1px 3px rgba(0,0,0,.08)}
  .cover__shapes{position:absolute;inset:0;width:100%;height:100%}

  .cover__org{position:absolute;left:28px;top:20px;color:var(--navy)}
  .cover__org-name{font-weight:800;font-size:22px;letter-spacing:1px;display:flex;align-items:center;gap:8px}
  .cover__org-dot{width:9px;height:9px;border-radius:50%;background:var(--navy)}
  .cover__org-full{margin-top:4px;font-weight:600;font-size:9.5px;line-height:1.15;width:150px}
  .cover__org-tag{margin-top:3px;font-weight:400;font-size:5px;letter-spacing:.3px}

  .cover__title{position:absolute;left:30px;top:410px;color:var(--title);font-weight:900;font-size:62px;line-height:.98;letter-spacing:1px}
  .cover__subtitle{position:absolute;left:32px;top:546px;color:var(--subtitle);font-weight:300;font-size:27px;letter-spacing:.2px}

  .cover__badge{position:absolute;right:18px;bottom:28px;width:46px;height:46px;border-radius:50%;background:var(--badge)}
</style>
</head>
<body>
  <main class="binder">
    <section class="spine" aria-label="Binder spine">
      <svg class="spine__shapes" viewBox="0 0 138 640" preserveAspectRatio="none" aria-hidden="true">
        <polygon points="0,0 138,0 138,205 0,110" fill="var(--navy)"/>
        <polygon points="0,110 138,205 0,310" fill="var(--sky)"/>
        <polygon points="138,205 138,330 70,355 0,310" fill="var(--royal)"/>
        <polygon points="0,310 138,330 0,430" fill="var(--royal)"/>
      </svg>
      <div class="spine__mark">NCLFA</div>
      <h2 class="spine__title">SUMMIT<br>INSTITUTE</h2>
      <div class="spine__band"></div>
    </section>

    <section class="cover" aria-label="Binder front cover">
      <svg class="cover__shapes" viewBox="0 0 1000 1000" preserveAspectRatio="none">
        <defs>
          <linearGradient id="photoTone" x1="0" y1="0" x2="1" y2="1">
            <stop offset="0" stop-color="var(--photo-b)"/>
            <stop offset=".55" stop-color="#8a98a8"/>
            <stop offset="1" stop-color="var(--photo-a)"/>
          </linearGradient>
        </defs>
        <polygon role="img" aria-label="Photo of tax professionals reviewing charts on a laptop and tablet at a desk"
          points="300,0 1000,0 1000,740 780,720 330,180 0,400 0,230" fill="url(#photoTone)"/>
        <polygon points="300,0 690,0 330,180 0,380 0,230" fill="var(--tint)" opacity=".55" aria-hidden="true"/>
        <polygon points="0,180 100,255 0,370" fill="var(--navy)" aria-hidden="true"/>
        <polygon points="780,720 1000,560 1000,900" fill="var(--royal)" aria-hidden="true"/>
      </svg>

      <div class="cover__org">
        <div class="cover__org-name"><span class="cover__org-dot"></span>NCLFA</div>
        <div class="cover__org-full">National Council of Levy Fixers Alliance</div>
        <div class="cover__org-tag">A NON-PROFIT PROFESSIONAL ASSOCIATION</div>
      </div>

      <h1 class="cover__title">SUMMIT<br>INSTITUTE</h1>
      <p class="cover__subtitle">FRB Tax Problem Resolution</p>

      <div class="cover__badge" role="img" aria-label="Accreditation sponsor badge"></div>
      <div class="cover__band"></div>
    </section>
  </main>
</body>
</html>
```